Maison Corvel

I am actually making my own traditional french food.
Everything is homemade with passion.
I make differente terrines, jams, macaroons, rillettes and much more
I do as well cocktail party and catering
Updates

Hello everyone,

On the business card I would like to see appear if it's possible these following informations: traditional french food, cocktail party and catering.

Industry/Entity Type

Catering

```html
<!DOCTYPE html>
<html lang="en">
<head>
<meta charset="utf-8">
<title>Maison Corvel – Business Card</title>
<link rel="stylesheet" href="https://fonts.googleapis.com/css2?family=Open+Sans:wght@400;600;700&display=swap">
<style>
  :root {
    --backdrop: #ecebe8;
    --card-white: #ffffff;
    --brand-red: #c01f2f;
    --ink: #1d1d1d;
    --rule-grey: #9a9a9a;
    --text-dark: #2a2a2a;
  }
  * { margin: 0; padding: 0; box-sizing: border-box; }
  html, body {
    width: 1162px;
    height: 1200px;
    overflow: hidden;
    background: var(--backdrop);
    font-family: "Open Sans", Arial, sans-serif;
  }
  .canvas { position: relative; width: 1162px; height: 1200px; }

  /* Front card */
  .card-front {
    position: absolute;
    left: 173px; top: 35px;
    width: 949px; height: 545px;
    background: var(--card-white);
    box-shadow: 0 2px 6px rgba(0,0,0,0.18);
  }
  .edge-tab {
    position: absolute;
    top: 101px; width: 22px; height: 355px;
  }
  .edge-tab--left { left: 0; background: var(--brand-red); border-radius: 0 12px 12px 0; }
  .edge-tab--right { right: 0; background: var(--ink); border-radius: 12px 0 0 12px; }

  .brand-dot {
    position: absolute;
    left: 249px; top: 170px;
    width: 100px; height: 100px;
    border-radius: 50%;
    background: var(--brand-red);
  }
  .brand-name {
    position: absolute;
    left: 99px; top: 322px;
    width: 400px;
    text-align: center;
    font-size: 40px;
    font-weight: 700;
    letter-spacing: 1px;
    line-height: 1.2;
    color: var(--ink);
    text-transform: uppercase;
  }
  .brand-services {
    position: absolute;
    left: 99px; top: 384px;
    width: 400px;
    text-align: center;
    font-size: 17px;
    font-weight: 600;
    line-height: 24px;
    letter-spacing: 0.5px;
    color: var(--brand-red);
  }

  .divider {
    position: absolute;
    left: 558px; top: 170px;
    width: 1px; height: 203px;
    background: var(--rule-grey);
  }
  .contact {
    position: absolute;
    left: 582px; top: 178px;
  }
  .contact__name {
    font-size: 31px;
    font-weight: 600;
    color: var(--brand-red);
    line-height: 1.2;
    margin-bottom: 28px;
  }
  .contact__line {
    display: flex;
    align-items: center;
    gap: 8px;
    font-size: 22px;
    color: var(--text-dark);
    height: 42px;
  }
  .contact__icon { width: 18px; height: 18px; flex: none; }

  /* Back card */
  .card-back {
    position: absolute;
    left: 29px; top: 614px;
    width: 951px; height: 543px;
    background: var(--brand-red);
    box-shadow: 0 2px 6px rgba(0,0,0,0.18);
  }
  .back-name {
    position: absolute;
    left: 144px; top: 300px;
    width: 662px;
    text-align: center;
    font-size: 56px;
    font-weight: 700;
    letter-spacing: 2px;
    color: #ffffff;
    text-transform: uppercase;
  }
  .back-rule {
    position: absolute;
    left: 144px; top: 407px;
    width: 662px; height: 8px;
    background: #ffffff;
  }
  .back-web {
    position: absolute;
    left: 0; top: 470px;
    width: 100%;
    text-align: center;
    font-size: 27px;
    letter-spacing: 2px;
    color: #ffffff;
  }
</style>
</head>
<body>
<main class="canvas">
  <section class="card-front">
    <div class="edge-tab edge-tab--left"></div>
    <div class="edge-tab edge-tab--right"></div>

    <div class="brand-dot"></div>
    <div class="brand-name">Maison Corvel</div>
    <p class="brand-services">Traditional French food<br>Cocktail party &amp; catering</p>

    <div class="divider"></div>

    <div class="contact">
      <p class="contact__name">Julien Marchetti</p>
      <p class="contact__line">
        <svg class="contact__icon" viewBox="0 0 20 20" aria-hidden="true">
          <circle cx="10" cy="10" r="9" fill="none" stroke="#c01f2f" stroke-width="2"/>
          <path d="M7 5.5 l2 2 -1.2 1.4 c.7 1.5 1.8 2.6 3.3 3.3 l1.4-1.2 2 2 -1.6 1.6 c-3.5-.6-6.9-4-7.5-7.5z" fill="#c01f2f"/>
        </svg>
        042-5550-173
      </p>
      <p class="contact__line">
        <svg class="contact__icon" viewBox="0 0 20 20" aria-hidden="true">
          <rect x="1" y="4" width="18" height="12" rx="1.5" fill="#c01f2f"/>
          <path d="M1.5 5 L10 11 L18.5 5" fill="none" stroke="#fff" stroke-width="1.6"/>
        </svg>
        julien.m@corvel.fr
      </p>
      <p class="contact__line">ABN: 98765432100</p>
    </div>
  </section>

  <section class="card-back">
    <div class="back-name">Maison Corvel</div>
    <div class="back-rule"></div>
    <p class="back-web">www.maisoncorvel.com</p>
  </section>
</main>
</body>
</html>
```